Set up small scale company website

We need a website set up for our educational consultancy - Brellin Learning. We like the following site and want something similar www.quorvadeplan.co.uk We can provide the copy and images but need the following:- setting up the overall theme and design - to our requirements on colours and forma- Approximately 4 pages of services offered and with an index pageEtct (yellow and green)And the following pages - as well as a home page:- A contact page linked to our email addresses and registered business address 17 Millbrook Lane, Harwich, Essex, CO12 5JP- About Us page - An index of services page that links to between 4-6 pages outlining services- A News page that links to updates of latest services, events and activities - easily updated by usOn the homepage we'd like links to twitter and LinkedIn feeds and links to our other blogs and websites
Target Market(s)
Schools, local authoroties and multi-academy trusts
Logo Text
Brellin Learning
Coding
Coded - Design and coding required
Number of Pages Required
5+ page
Font styles to use
Requirements
Should not have
- No tacky pictures of mortar boards or chalk boards etc.

```html
<!DOCTYPE html>
<html lang="en">
<head>
<meta charset="utf-8">
<title>Brellin Learning</title>
<link rel="stylesheet" href="https://fonts.googleapis.com/css2?family=Lato:wght@400;700&display=swap">
<style>
:root{
  --green:#74ae00;
  --green-dark:#4f9a13;
  --yellow:#e6d000;
  --yellow-light:#f3e640;
  --cream:#fdf6c3;
  --bar:#f0f0f0;
  --ink:#222;
  --text:#444;
  --link:#1a8ac4;
  --rule:#d8d8d8;
}
*{box-sizing:border-box;margin:0;padding:0}
html,body{width:1159px;height:1200px;overflow:hidden;background:#fff}
body{position:relative;font-family:"Lato",sans-serif;color:var(--text)}
.abs{position:absolute}

.topbar{left:0;top:0;width:1159px;height:47px;background:var(--bar)}
.contact-item{top:0;height:47px;display:flex;align-items:center;gap:12px;font-size:13.5px;color:var(--ink);letter-spacing:.3px}
.social{top:0;height:47px;display:flex}
.social-slot{width:61px;height:47px;border-left:1px solid #d6d6d6;display:flex;align-items:center;justify-content:center}
.social-slot:last-child{border-right:1px solid #d6d6d6}
.social-dot{width:16px;height:16px;border-radius:50%;background:#c9b300}

.header{left:0;top:47px;width:1159px;height:79px;background:#fff}
.brand{left:111px;top:0;height:79px;display:flex;align-items:center;font-size:22px;font-weight:700;color:var(--green-dark);letter-spacing:.5px}
.nav-item{top:0;height:79px;display:flex;align-items:center;font-size:13px;color:var(--ink);letter-spacing:.4px}
.nav-item.active{left:673px;width:97px;justify-content:center;background:linear-gradient(135deg,var(--yellow-light),var(--yellow));color:#333}

.hero{left:0;top:126px;width:1159px;height:319px;background:linear-gradient(180deg,#7d6683 0%,#a07f7d 45%,#c7946a 70%,#4e3a55 100%)}
.hero-text{left:0;top:52px;width:1287px;text-align:center;color:#fff;font-weight:700;text-shadow:0 2px 4px rgba(0,0,0,.3)}
.hero-line{font-size:37px;line-height:46px;letter-spacing:1px}
.hero-line.small{font-size:33px;line-height:38px}
.dots{left:547px;top:301px;display:flex;gap:7px}
.dot{width:15px;height:8px;background:#111}
.dot.on{background:var(--yellow)}

.tile{top:460px;width:128px;height:128px;background:var(--green);color:#fff;font-weight:700;font-size:12.5px;text-align:center;letter-spacing:.3px}
.tile.active{background:linear-gradient(135deg,var(--yellow-light),var(--yellow))}
.tile-icon{position:absolute;left:34px;top:12px;width:60px;height:60px;border-radius:6px;background:rgba(255,255,255,.28)}
.tile-label{position:absolute;left:0;bottom:8px;width:100%;line-height:16px}

.welcome-title{left:0;top:614px;width:1287px;text-align:center;font-size:21px;font-weight:700;color:#444;letter-spacing:.3px}
.welcome-copy{left:113px;top:654px;width:970px;font-size:14.4px;line-height:25.4px;color:#555;letter-spacing:.2px}

.feed{left:0;top:793px;width:1159px;height:407px;background:var(--cream)}
.feed-art{left:567px;top:15px;width:76px;height:76px;background:#e9e1a8;border-radius:4px}
.arrows{left:1012px;top:15px;display:flex;gap:2px}
.arrow{width:42px;height:31px;background:var(--green);display:flex;align-items:center;justify-content:center}

.card{top:110px;width:189px;height:268px;background:#fff;border:1px solid #d6d6d6;padding:18px 6px 0 7px}
.card-copy{font-size:12.3px;line-height:25.4px;color:#444;letter-spacing:.2px}
.card-link{font-size:12.3px;color:var(--link);margin-top:-1px}
.card-rule{height:1px;background:var(--rule);margin:16px 7px 14px 7px}
.card-title{font-size:16px;color:var(--link);letter-spacing:.3px}
.card-date{font-size:12.5px;color:#333}
</style>
</head>
<body>

<div class="abs topbar">
  <div class="abs contact-item" style="left:110px">
    <svg width="21" height="20" viewBox="0 0 24 24"><path fill="#c9a800" d="M6.6 10.8a15.1 15.1 0 0 0 6.6 6.6l2.2-2.2a1 1 0 0 1 1-.25 11.4 11.4 0 0 0 3.6.57 1 1 0 0 1 1 1V20a1 1 0 0 1-1 1A17 17 0 0 1 3 4a1 1 0 0 1 1-1h3.5a1 1 0 0 1 1 1c0 1.25.2 2.45.57 3.57a1 1 0 0 1-.25 1z"/></svg>
    <span style="margin-left:4px">61 470 385</span>
  </div>
  <div class="abs contact-item" style="left:250px">
    <svg width="20" height="15" viewBox="0 0 20 15"><rect width="20" height="15" rx="1.5" fill="#c9a800"/><path d="M1 1.5l9 6.5 9-6.5" fill="none" stroke="#f0f0f0" stroke-width="1.6"/></svg>
    <span style="margin-left:4px">hello@brellinlearning.com</span>
  </div>
  <div class="abs social" style="left:915px">
    <div class="social-slot"><span class="social-dot"></span></div>
    <div class="social-slot"><span class="social-dot"></span></div>
    <div class="social-slot"><span class="social-dot"></span></div>
  </div>
</div>

<header class="abs header">
  <div class="abs brand">BRELLIN LEARNING</div>
  <nav>
    <a class="abs nav-item" style="left:603px">HOME</a>
    <a class="abs nav-item active">SERVICES</a>
    <a class="abs nav-item" style="left:804px">NEWS</a>
    <a class="abs nav-item" style="left:898px">ABOUT US</a>
    <a class="abs nav-item" style="left:1012px">CONTACT</a>
  </nav>
</header>

<section class="abs hero" role="img" aria-label="Photograph of graduates silhouetted against a sunset sky">
  <div class="abs hero-text">
    <div class="hero-line">PASSION</div>
    <div class="hero-line">L<svg width="32" height="30" viewBox="0 0 32 30" style="vertical-align:-3px"><path fill="#fff" d="M16 29S1 19 1 9.5A7.5 7.5 0 0 1 16 6a7.5 7.5 0 0 1 15 3.5C31 19 16 29 16 29z"/></svg>VING</div>
    <div class="hero-line small">What we do</div>
  </div>
  <div class="abs dots"><span class="dot"></span><span class="dot on"></span><span class="dot"></span><span class="dot"></span></div>
</section>

<section class="services">
  <div class="abs tile" style="left:109px"><span class="tile-icon" role="img" aria-label="Finance icon"></span><span class="tile-label">FINANCE</span></div>
  <div class="abs tile" style="left:282px"><span class="tile-icon" role="img" aria-label="Personnel icon"></span><span class="tile-label">PERSONNEL</span></div>
  <div class="abs tile active" style="left:454px"><span class="tile-icon" role="img" aria-label="Facilities icon"></span><span class="tile-label">FACILITIES</span></div>
  <div class="abs tile" style="left:626px"><span class="tile-icon" role="img" aria-label="Academy conversion icon"></span><span class="tile-label">ACADEMY<br>CONVERSION</span></div>
  <div class="abs tile" style="left:799px"><span class="tile-icon" role="img" aria-label="Staff solution icon"></span><span class="tile-label">STAFF<br>SOLUTION</span></div>
  <div class="abs tile" style="left:971px"><span class="tile-icon" role="img" aria-label="Auditing icon"></span><span class="tile-label">AUDITING</span></div>
</section>

<h1 class="abs welcome-title">Welcome to Brellin Learning</h1>
<p class="abs welcome-copy">Lorem ipsum dolor sit amet, consectetur adipiscing elit, sed do eiusmod tempor incididunt ut labore et dolore magna aliqua. Ut enim ad minim veniam, quis nostrud exercitation ullamco laboris nisi ut aliquip ex ea commodo consequat. Duis aute irure dolor in reprehenderit in voluptate velit esse cillum dolore eu fugiat nulla pariatur. Excepteur sint occaecat cupidatat non proident, sunt in culpa qui officia deserunt mollit anim id est laborum.</p>

<section class="abs feed">
  <div class="abs feed-art" role="img" aria-label="Line illustration of a hand holding social media feeds"></div>
  <div class="abs arrows">
    <span class="arrow"><svg width="14" height="18" viewBox="0 0 14 18"><path d="M11 2L4 9l7 7" fill="none" stroke="#fff" stroke-width="3"/></svg></span>
    <span class="arrow"><svg width="14" height="18" viewBox="0 0 14 18"><path d="M3 2l7 7-7 7" fill="none" stroke="#fff" stroke-width="3"/></svg></span>
  </div>

  <article class="abs card" style="left:110px">
    <p class="card-copy">Lorem ipsum dolor sit amet, consectetur adipiscing elit, sed do eiusmod tempor incidi-dunt ut labore et dolore magna aliqua.</p>
    <p class="card-link">http://www.brellinlearning.com</p>
    <div class="card-rule"></div>
    <p class="card-title">Brellin Learning</p>
    <p class="card-date">Feb 5th</p>
  </article>
  <article class="abs card" style="left:376px">
    <p class="card-copy">Lorem ipsum dolor sit amet, consectetur adipiscing elit, sed do eiusmod tempor incidi-dunt ut labore et dolore magna aliqua.</p>
    <p class="card-link">http://www.brellinlearning.com</p>
    <div class="card-rule"></div>
    <p class="card-title">Brellin Learning</p>
    <p class="card-date">Feb 5th</p>
  </article>
  <article class="abs card" style="left:643px">
    <p class="card-copy">Lorem ipsum dolor sit amet, consectetur adipiscing elit, sed do eiusmod tempor incidi-dunt ut labore et dolore magna aliqua.</p>
    <p class="card-link">http://www.brellinlearning.com</p>
    <div class="card-rule"></div>
    <p class="card-title">Brellin Learning</p>
    <p class="card-date">Feb 5th</p>
  </article>
  <article class="abs card" style="left:909px">
    <p class="card-copy">Lorem ipsum dolor sit amet, consectetur adipiscing elit, sed do eiusmod tempor incidi-dunt ut labore et dolore magna aliqua.</p>
    <p class="card-link">http://www.brellinlearning.com</p>
    <div class="card-rule"></div>
    <p class="card-title">Brellin Learning</p>
    <p class="card-date">Feb 5th</p>
  </article>
</section>

</body>
</html>
```